Halvorsen Construction Needs a Business Card

Our current business card is very bland, and since we have a new logo, we would like a new business card design to reflect our company. It can be a single-sided or two-sided card, but it is important that our contact information appears on the same side. I am attaching a copy of our old card and our new logo. If you need the logo in another format than the one I'm sending, please let me know. This is the information that we must have on our card, but not necessarily in any specific order:
1) Our logo
2) General Contractor
3) Dale Halvorsen, Owner
4) 482 Commerce Ridge Road, Alderbrook, Fairhaven 35871
5) Office: 555-555-0147
7) Fax: 555-555-0148
8) Cell: 555-555-0193
9) halvorsenconstruction@qvl-mail.net
10) halvorsenconstruction-example.com (can be omitted if necessary)
Also, I will need files in a format that I can alter if any of the above information changes in the near future. Thank you in advance for your submissions!
Target Market(s)
Commercial and residential clients, architects, and subcontractors.
Industry/Entity Type
Business
Look and feel

```html
<!DOCTYPE html>
<html lang="en">
<head>
<meta charset="utf-8">
<title>Halvorsen Construction – Business Card</title>
<link href="https://fonts.googleapis.com/css2?family=Arimo:wght@400;700&display=swap" rel="stylesheet">
<style>
  :root {
    --backdrop: #e6e8ea;
    --silver-light: #c3c6c9;
    --silver-dark: #8f9397;
    --band-top: #2e2b2b;
    --band-bottom: #1c1a1a;
    --ink-dark: #1e1e1e;
    --ink-light: #ffffff;
    --ink-soft: #d9d9d9;
    --rule: #6d6a6a;
  }
  * { margin: 0; padding: 0; box-sizing: border-box; }
  html, body {
    width: 1200px;
    height: 800px;
    overflow: hidden;
    background: var(--backdrop);
    font-family: "Arimo", Arial, sans-serif;
  }
  .canvas {
    width: 1200px;
    height: 800px;
    display: flex;
    align-items: center;
    justify-content: center;
  }
  .business-card {
    position: relative;
    width: 840px;
    height: 480px;
    overflow: hidden;
    box-shadow: 0 10px 30px rgba(0,0,0,0.18);
  }
  .card-top {
    position: absolute;
    inset: 0 0 56% 0;
    background: radial-gradient(ellipse at 50% 20%, var(--silver-light), var(--silver-dark) 120%);
  }
  .card-band {
    position: absolute;
    inset: 44% 0 0 0;
    background: linear-gradient(180deg, var(--band-top), var(--band-bottom));
  }
  .brand {
    position: absolute;
    left: 0;
    right: 0;
    top: 128px;
    display: flex;
    align-items: center;
    justify-content: center;
    gap: 14px;
  }
  .brand-square {
    width: 44px;
    height: 44px;
    background: var(--ink-dark);
  }
  .brand-name {
    font-weight: 700;
    font-size: 34px;
    letter-spacing: 1px;
    color: var(--ink-dark);
    text-transform: uppercase;
  }
  .contact {
    position: absolute;
    left: 0;
    right: 0;
    top: 238px;
    text-align: center;
    color: var(--ink-soft);
  }
  .contact-name {
    font-size: 34px;
    font-weight: 400;
    color: var(--ink-light);
    letter-spacing: 0.3px;
  }
  .contact-rule {
    width: 420px;
    height: 1px;
    margin: 10px auto 8px;
    background: linear-gradient(90deg, transparent, var(--rule) 20%, var(--rule) 80%, transparent);
  }
  .contact-title {
    font-size: 15px;
    letter-spacing: 1.5px;
    color: var(--ink-light);
    margin-bottom: 12px;
  }
  .contact-line {
    font-size: 13px;
    line-height: 19px;
  }
</style>
</head>
<body>
  <main class="canvas">
    <article class="business-card">
      <div class="card-top"></div>
      <div class="card-band"></div>

      <div class="brand">
        <span class="brand-square" aria-hidden="true"></span>
        <span class="brand-name">Halvorsen Construction</span>
      </div>

      <section class="contact">
        <h1 class="contact-name">Dale Halvorsen, Owner</h1>
        <div class="contact-rule"></div>
        <p class="contact-title">GENERAL CONTRACTOR</p>
        <p class="contact-line">482 Commerce Ridge Road, Alderbrook, Fairhaven 35871</p>
        <p class="contact-line">T : 555-555-0193 | F : 555-555-0148 | Office : 555-555-0147</p>
        <p class="contact-line">halvorsenconstruction@qvl-mail.net</p>
      </section>
    </article>
  </main>
</body>
</html>
```